Offshore Energy Projects Management Consultancy needs a business card design

Logo available. We provide teams to deliver engineering consultancy, project management and delivery teams mainly in the offshore renewables sector. The company is all about bringing the right people to a project to deliver the scope.

The business card will be used for all staff.

The business card should be quite simple, vibrant and uncluttered but convey experience, enthusiasm and integration.

Target Market(s)

Energy Project Developers and Tier 1 construction companies

Contact Information for Business Card

Logo should be on the back of the card. I'm happy for the designer to play with the colour of the logo and background colour.

Front of the card should convey all the must have information in a clear and professional manner but without being overly traditional.

Colors

Designer to choose colors to be used in the design.

Requirements
Must have
• Land Line Tel Number, Mobile Tel Number, Email, business address, web address.

```html
<!DOCTYPE html>
<html lang="en">
<head>
<meta charset="utf-8">
<title>Business Card – Back and Front</title>
<link href="https://fonts.googleapis.com/css2?family=Oswald:wght@300;400;600&display=swap" rel="stylesheet">
<style>
  :root {
    --canvas: #d8d8d8;
    --card: #2f2f2f;
    --blue: #3f8fd0;
    --blue-deep: #2f5fb0;
    --white: #f2f2f2;
  }
  * { margin: 0; padding: 0; box-sizing: border-box; }
  html, body {
    width: 1200px; height: 1200px; overflow: hidden;
    background: var(--canvas);
    font-family: "Oswald", sans-serif;
  }
  .sheet {
    width: 1200px; height: 1200px;
    display: flex; flex-direction: column; align-items: center; justify-content: center;
    gap: 70px;
  }
  .card {
    position: relative;
    width: 840px; height: 480px;
    background: var(--card);
    box-shadow: 0 6px 18px rgba(0,0,0,0.18);
  }
  /* Back */
  .card--back { display: flex; align-items: center; justify-content: center; }
  .brand { display: flex; align-items: center; gap: 16px; color: var(--blue); white-space: nowrap; }
  .brand__dot { width: 26px; height: 26px; border-radius: 50%; background: var(--blue); flex: none; }
  .brand__name { font-weight: 400; letter-spacing: 3px; text-transform: uppercase; line-height: 1; }
  .card--back .brand__name { font-size: 40px; }
  /* Front */
  .rule {
    position: absolute; left: 0; top: 128px; width: 430px; height: 2px;
    background: var(--blue-deep);
  }
  .card--front .brand { position: absolute; right: 34px; top: 98px; gap: 12px; }
  .card--front .brand__dot { width: 20px; height: 20px; }
  .card--front .brand__name { font-size: 22px; letter-spacing: 2px; }
  .person { position: absolute; left: 60px; top: 270px; }
  .person__name {
    color: var(--white); font-weight: 600; font-size: 32px; letter-spacing: 2px; line-height: 1.1;
  }
  .person__title {
    color: var(--blue); font-weight: 300; font-size: 24px; letter-spacing: 4px; text-transform: uppercase;
  }
  .contact { position: absolute; left: 60px; top: 370px; color: var(--white); font-weight: 300; font-size: 22px; letter-spacing: 2px; }
  .contact__row { display: flex; align-items: baseline; gap: 18px; line-height: 1.7; white-space: nowrap; }
  .contact__label { color: var(--blue); font-weight: 400; margin-right: 6px; }
</style>
</head>
<body>
<main class="sheet">
  <section class="card card--back" aria-label="Card back">
    <div class="brand">
      <span class="brand__dot"></span>
      <span class="brand__name">Keelhaven Project Collective</span>
    </div>
  </section>

  <section class="card card--front" aria-label="Card front">
    <div class="rule"></div>
    <div class="brand">
      <span class="brand__dot"></span>
      <span class="brand__name">Keelhaven Project Collective</span>
    </div>
    <div class="person">
      <p class="person__name">ELIN MARSH</p>
      <p class="person__title">Title Here</p>
    </div>
    <div class="contact">
      <p class="contact__row">
        <span><span class="contact__label">P.</span>555.210.4431</span>
        <span>|</span>
        <span><span class="contact__label">P.</span>555.210.4432</span>
        <span>|</span>
        <span><span class="contact__label">E.</span>elin@keelhaven.example</span>
      </p>
      <p class="contact__row">
        <span><span class="contact__label">A.</span>48 Harbour Row, Northport, ME. 04950</span>
      </p>
    </div>
  </section>
</main>
</body>
</html>
```